creation of a postcard style drop off marketing vehicle..

WE GO LIVE

take a peek at my website to best understand my business. www.wegolive.com.

my business is recording young musicians (vocalist and instrumentalists) both video and audio. professional recordings produced at a price which a young artist can afford. i would like the postcard to help a prospect for my services to be able to visualize themselves performing in a recording studio. that, along with some titling which supports the image and provides contact data . i will use the postcard as both a drop off piece and as a piece to pin on a public announcement board. i need a business card which mimics the postcard with just contact data.

Professional and Affordable Video Recordings of Your Performance

High Quality Video Files (MPEG 4/H.264 Files) For Distribution Across
Internet, Social Media, Flickbay, Streamora, Or Embedding In Your Website.

www.WEGOLIVE.rocks

kelpbarn@mailnest.net
calvin brostoff
555-271-0846

```html
<!DOCTYPE html>
<html lang="en">
<head>
<meta charset="utf-8">
<title>WE GO LIVE — Postcard and Business Card</title>
<link rel="stylesheet" href="https://fonts.googleapis.com/css2?family=Josefin+Sans:wght@100;300&family=Jost:wght@400&family=Cinzel:wght@400&display=swap">
<style>
  :root {
    --backdrop: #d9d4cc;
    --card-black: #0c0c0d;
    --band-grey: rgba(64, 64, 66, 0.78);
    --studio-deep: #0f0f10;
    --studio-dark: #1d1d1f;
    --studio-mid: #38383b;
    --studio-light: #77777b;
    --studio-glow: #9a9a9e;
    --gold: #c9a968;
    --gold-soft: #b39560;
    --text-light: #f2f2f2;
    --text-muted: #d6d6d6;
    --frame-light: #cfcfcf;
  }
  * { box-sizing: border-box; margin: 0; padding: 0; }
  html, body { width: 1200px; height: 882px; overflow: hidden; }
  body { background: var(--backdrop); position: relative; font-family: "Jost", "Futura", sans-serif; }

  .postcard, .business-card {
    position: absolute;
    background: var(--card-black);
    overflow: hidden;
    box-shadow: 0 4px 16px rgba(0,0,0,0.35);
  }
  .postcard { left: 175px; top: 87px; width: 478px; height: 736px; }
  .business-card { left: 766px; top: 260px; width: 260px; height: 439px; }

  .studio-photo {
    position: absolute; left: 0; right: 0; top: 0;
    background:
      radial-gradient(ellipse 14% 26% at 62% 40%, var(--studio-glow) 0%, rgba(119,119,123,0.55) 45%, rgba(0,0,0,0) 100%),
      radial-gradient(ellipse 30% 22% at 64% 62%, rgba(90,90,94,0.6) 0%, rgba(0,0,0,0) 100%),
      radial-gradient(circle at 18% 36%, rgba(80,80,84,0.55) 0%, rgba(0,0,0,0) 22%),
      radial-gradient(ellipse 18% 48% at 96% 40%, rgba(110,110,114,0.45) 0%, rgba(0,0,0,0) 100%),
      linear-gradient(180deg, var(--studio-deep) 0%, var(--studio-mid) 30%, var(--studio-dark) 65%, var(--studio-deep) 100%);
  }
  .postcard .studio-photo { height: 736px; }
  .business-card .studio-photo { height: 300px; }

  .contact-base {
    position: absolute; left: 0; right: 0; bottom: 0; height: 96px;
    background: linear-gradient(180deg, rgba(12,12,13,0) 0%, rgba(12,12,13,0.85) 45%, var(--card-black) 100%);
  }

  .title-band {
    position: absolute; left: 0; right: 0;
    background: var(--band-grey);
    text-align: center;
  }
  .postcard .title-band { top: 42px; height: 112px; }
  .business-card .title-band { top: 32px; height: 52px; }

  .brand-name {
    font-family: "Josefin Sans", sans-serif;
    font-weight: 100;
    color: var(--gold);
    letter-spacing: 0.02em;
    line-height: 1;
  }
  .postcard .brand-name { font-size: 58px; padding-top: 14px; }
  .business-card .brand-name { font-size: 28px; padding-top: 8px; }

  .tagline {
    font-family: "Cinzel", serif;
    color: var(--gold-soft);
    letter-spacing: 0.12em;
    white-space: nowrap;
  }
  .postcard .tagline { font-size: 9.5px; margin-top: 20px; }
  .business-card .tagline { font-size: 5.2px; margin-top: 6px; }

  .headline {
    position: absolute; left: 12px; top: 432px;
    color: var(--text-light);
    font-weight: 400;
    font-size: 23px;
    line-height: 1.26;
    text-shadow: 0 1px 3px rgba(0,0,0,0.7);
  }
  .headline .line-two { display: block; padding-left: 80px; }

  .thumb-strip { position: absolute; left: 0; top: 536px; width: 478px; height: 84px; }

  .contact-row {
    position: absolute; left: 0; right: 0; top: 682px;
    display: flex; justify-content: center; gap: 14px;
    color: var(--text-muted); font-size: 14.5px;
  }
  .contact-item { display: flex; align-items: center; gap: 4px; white-space: nowrap; }
  .contact-icon { width: 13px; height: 13px; flex: none; }

  .holder-name {
    position: absolute; left: 22px; top: 299px;
    color: var(--text-light); font-size: 13.5px; letter-spacing: 0.03em;
  }
  .gold-rule { position: absolute; left: 0; right: 0; top: 320px; height: 1.5px; background: var(--gold); }
  .card-contacts {
    position: absolute; left: 22px; top: 326px;
    list-style: none; color: var(--text-muted); font-size: 12px;
  }
  .card-contacts li { display: flex; align-items: center; gap: 5px; height: 23px; }
  .card-contacts .contact-icon { width: 10px; height: 10px; }

  .card-foot { position: absolute; left: 0; top: 410px; width: 260px; height: 29px; }
</style>
</head>
<body>

<section class="postcard">
  <div class="studio-photo" role="img" aria-label="Studio condenser microphone with pop filter in front of acoustic foam wall"></div>
  <div class="contact-base"></div>
  <header class="title-band">
    <h1 class="brand-name">WE GO LIVE</h1>
    <p class="tagline">VIDEOGRAPHIC RECORDINGS FOR VOCALISTS, MUSICIANS AND THEATRE</p>
  </header>
  <h2 class="headline">Professional and Affordable Video<span class="line-two">Recordings of Your Performance</span></h2>

  <svg class="thumb-strip" viewBox="0 0 478 84">
    <defs>
      <linearGradient id="thumb-red" x1="0" y1="0" x2="1" y2="1">
        <stop offset="0" stop-color="#a3151b"/><stop offset="0.6" stop-color="#6b1014"/><stop offset="1" stop-color="#2a2222"/>
      </linearGradient>
      <linearGradient id="thumb-grey" x1="0" y1="0" x2="1" y2="1">
        <stop offset="0" stop-color="#8a8a8a"/><stop offset="0.5" stop-color="#4a4a4a"/><stop offset="1" stop-color="#9a1a1e"/>
      </linearGradient>
      <linearGradient id="thumb-warm" x1="0" y1="0" x2="1" y2="1">
        <stop offset="0" stop-color="#c8c4bd"/><stop offset="0.55" stop-color="#5b4a44"/><stop offset="1" stop-color="#7e1d1d"/>
      </linearGradient>
    </defs>
    <g role="img" aria-label="Recording studio room with piano and lights">
      <path d="M0 6 H150 Q158 6 155 14 L132 74 Q129 80 121 80 H0 Z" fill="url(#thumb-red)" stroke="var(--frame-light)" stroke-width="3"/>
    </g>
    <g role="img" aria-label="Studio set with camera and stage lights">
      <path d="M173 6 H305 Q313 6 310 14 L287 74 Q284 80 276 80 H148 Q140 80 143 72 L165 13 Q168 6 173 6 Z" fill="url(#thumb-grey)" stroke="var(--frame-light)" stroke-width="3"/>
    </g>
    <g role="img" aria-label="Guitarist performing in the studio">
      <path d="M328 6 H478 V80 H303 Q295 80 298 72 L320 13 Q323 6 328 6 Z" fill="url(#thumb-warm)" stroke="var(--frame-light)" stroke-width="3"/>
    </g>
  </svg>

  <div class="contact-row">
    <span class="contact-item">
      <svg class="contact-icon" viewBox="0 0 12 12"><circle cx="6" cy="6" r="6" fill="var(--gold)"/><circle cx="6" cy="6" r="3" fill="none" stroke="#3a2e1a" stroke-width="1"/></svg>
      www.WEGOLIVE.rocks
    </span>
    <span class="contact-item">
      <svg class="contact-icon" viewBox="0 0 12 12"><circle cx="6" cy="6" r="6" fill="var(--gold)"/><rect x="3" y="4" width="6" height="4" fill="none" stroke="#3a2e1a" stroke-width="0.9"/></svg>
      kelpbarn@mailnest.net
    </span>
    <span class="contact-item">
      <svg class="contact-icon" viewBox="0 0 12 12"><circle cx="6" cy="6" r="6" fill="var(--gold)"/><path d="M4 3.5 Q3 6 6 8.5 L7.5 7.5 L8.5 8.5 Q7 10 5 8.5 Q2.5 6.5 3 4 Z" fill="#3a2e1a"/></svg>
      555-271-0846
    </span>
  </div>
</section>

<section class="business-card">
  <div class="studio-photo" role="img" aria-label="Studio condenser microphone with pop filter in front of acoustic foam wall"></div>
  <header class="title-band">
    <h1 class="brand-name">WE GO LIVE</h1>
    <p class="tagline">VIDEOGRAPHIC RECORDINGS FOR VOCALISTS, MUSICIANS AND THEATRE</p>
  </header>
  <p class="holder-name">CALVIN BROSTOFF</p>
  <div class="gold-rule"></div>
  <ul class="card-contacts">
    <li><svg class="contact-icon" viewBox="0 0 12 12"><circle cx="6" cy="6" r="6" fill="var(--gold)"/></svg>www.WEGOLIVE.rocks</li>
    <li><svg class="contact-icon" viewBox="0 0 12 12"><rect x="0" y="2" width="12" height="8" fill="var(--gold)"/><path d="M0 2 L6 7 L12 2" fill="none" stroke="#3a2e1a" stroke-width="1"/></svg>kelpbarn@mailnest.net</li>
    <li><svg class="contact-icon" viewBox="0 0 12 12"><path d="M2.5 1 L5 1 L5.5 4 L4 5 Q5 7.5 7 8 L8 6.5 L11 7 L11 9.5 Q10 11 8 11 Q2 9.5 1 3 Q1 1.5 2.5 1 Z" fill="var(--gold)"/></svg>555-271-0846</li>
  </ul>
  <svg class="card-foot" viewBox="0 0 260 29" aria-hidden="true">
    <rect width="260" height="29" fill="#141414"/>
    <polygon points="0,2 52,2 44,29 0,29" fill="#5a5040"/>
    <polygon points="56,2 118,2 110,29 48,29" fill="#6e6048"/>
    <polygon points="122,2 184,2 176,29 114,29" fill="#8a7552"/>
    <polygon points="188,2 260,2 260,29 180,29" fill="#b39863"/>
  </svg>
</section>

</body>
</html>
```